Business card and stationery for new company
Member of Verola Group
Business card and stationery for new company - Aviation
Creative Brief
Professional
Bayu Santoso Wiratmaja
Managing Director
Jalan Cemara Lestari III no 8 Sukamulya Tengah South Jakarta 12450
+62 21 57186324 (Ext 204)
bayu.wiratmaja@verola-group.example

```html
<!DOCTYPE html>
<html lang="en">
<head>
<meta charset="utf-8">
<title>Cakra Langit Nusantara – Business Card</title>
<link href="https://fonts.googleapis.com/css2?family=Arimo:ital,wght@0,400;0,700;1,700&display=swap" rel="stylesheet">
<style>
  :root {
    --bg: #d9d9d7;
    --card: #ffffff;
    --navy: #3a2e96;
    --ink: #4a4a4a;
    --grey: #9a9a9a;
    --radius: 30px;
  }
  html, body {
    margin: 0;
    padding: 0;
    width: 1200px;
    height: 799px;
    overflow: hidden;
    background: var(--bg);
    font-family: "Arimo", Arial, sans-serif;
  }
  .canvas {
    position: relative;
    width: 1200px;
    height: 799px;
  }
  .card {
    position: absolute;
    width: 500px;
    height: 305px;
    background: var(--card);
    border-radius: var(--radius);
    overflow: hidden;
    box-shadow: 0 6px 18px rgba(0,0,0,0.18);
  }
  .card--back { left: 70px; top: 140px; }
  .card--front { left: 630px; top: 350px; }

  .brand {
    position: absolute;
    color: var(--navy);
    font-weight: 400;
    line-height: 1.15;
  }
  .card--back .brand {
    left: 0; right: 0;
    top: 110px;
    text-align: center;
    font-size: 30px;
  }
  .card--back .website {
    position: absolute;
    left: 0; right: 0;
    top: 220px;
    text-align: center;
    font-size: 12px;
    color: var(--ink);
  }
  .card--front .brand {
    left: 200px;
    top: 34px;
    font-size: 24px;
  }
  .holder {
    position: absolute;
    left: 26px;
    top: 150px;
  }
  .holder__name {
    margin: 0;
    color: var(--navy);
    font-size: 17px;
    font-weight: 700;
    font-style: italic;
  }
  .holder__title {
    margin: 3px 0 0 52px;
    font-size: 11px;
    color: var(--ink);
  }
  .contact {
    position: absolute;
    left: 262px;
    top: 104px;
    margin: 0;
    padding: 0;
    list-style: none;
    font-size: 11px;
    color: var(--ink);
    line-height: 15px;
  }
  .contact__address { margin-bottom: 3px; }
  .contact__item {
    position: relative;
    padding-left: 14px;
  }
  .contact__item::before {
    content: "";
    position: absolute;
    left: 0;
    top: 4px;
    width: 8px;
    height: 8px;
    border-radius: 50%;
    background: var(--navy);
  }
  .wave {
    position: absolute;
    left: 0;
    bottom: 0;
    width: 500px;
    height: 305px;
  }
</style>
</head>
<body>
<main class="canvas">
  <section class="card card--back">
    <div class="brand">Cakra Langit<br>Nusantara</div>
    <div class="website">www.verola-group.example</div>
  </section>

  <section class="card card--front">
    <svg class="wave" viewBox="0 0 500 305" aria-hidden="true">
      <path d="M0 214 C150 196 330 232 500 246" fill="none" stroke="var(--grey)" stroke-width="6"/>
      <path d="M0 226 C150 208 330 246 500 262 L500 305 L0 305 Z" fill="var(--navy)"/>
      <path d="M0 226 C150 208 330 246 500 262" fill="none" stroke="#ffffff" stroke-width="3"/>
    </svg>
    <div class="brand">Cakra Langit Nusantara</div>
    <div class="holder">
      <p class="holder__name">Bayu Santoso Wiratmaja</p>
      <p class="holder__title">Managing Director</p>
    </div>
    <ul class="contact">
      <li class="contact__address">Jalan Cemara Lestari III no 8<br>Sukamulya Tengah, South Jakarta 12450</li>
      <li class="contact__item">+62 21 57186324 (Ext 204)</li>
      <li class="contact__item">+62 81 3457921</li>
      <li class="contact__item">+62 21 57186330</li>
      <li class="contact__item">bayu.wiratmaja@verola-group.example</li>
      <li class="contact__item">www.verola-group.example</li>
    </ul>
  </section>
</main>
</body>
</html>
```